Water bottle logo and other essentials and accessories

Hello,

We have an exclusive villa in Italy where our guests get free water from our bottles as a courtesy. (as well as wine, beer etc)

We ordered 1000 bottles and it seems like we can have our Logo and/or house name on the bottles.

Well.. we have a house name( Villa Serena), but not a logo.

If the bottle Logo ends good we will continue to use the logo in the future.

The Villa is high end, by the mediterranean sea.

Target Market(s)

High end travelers

Industry/Entity Type

Real Estate

Font styles to use
Decorative
Script

Colors

Designer to choose colors to be used in the design.

Requirements
Must have
• Class
Nice to have
• Imagine "Kelda Water".
Should not have
• Tropical colors
• Hello, I like your idea here.
• Just to be precise: The Kelda water picture I added is just for inspiration.
• If possible you can write:
• Acqua Minerale and Acqua Frizzante instead

```html
<!DOCTYPE html>
<html lang="en">
<head>
<meta charset="utf-8">
<title>Villa Serena – Sparkling Water Label</title>
<link rel="stylesheet" href="https://fonts.googleapis.com/css2?family=Ubuntu:wght@500&family=Lato:wght@300&family=Arimo&display=swap">
<style>
  :root {
    --page: #ffffff;
    --label: #000000;
    --gold: #c8923f;
    --ink-light: #ffffff;
  }
  html, body {
    margin: 0;
    padding: 0;
    width: 1200px;
    height: 1200px;
    overflow: hidden;
    background: var(--page);
  }
  .canvas {
    position: relative;
    width: 1200px;
    height: 1200px;
    background: var(--page);
  }
  .label {
    position: absolute;
    left: 202px;
    top: 307px;
    width: 796px;
    height: 586px;
    background: var(--label);
    overflow: hidden;
  }
  .wordmark {
    position: absolute;
    margin: 0;
    font-family: "Ubuntu", sans-serif;
    font-weight: 500;
    color: var(--gold);
    white-space: nowrap;
    line-height: 1;
  }
  .wordmark--hero {
    left: 505px;
    top: 531px;
    font-size: 86px;
    transform: rotate(-90deg);
    transform-origin: 0 0;
  }
  .product-info {
    position: absolute;
    left: 606px;
    top: 286px;
    font-family: "Lato", sans-serif;
    font-weight: 300;
    color: var(--ink-light);
    text-align: left;
    line-height: 1.1;
  }
  .product-info__type {
    font-size: 14px;
    letter-spacing: 0.3px;
    margin: 0;
  }
  .product-info__volume {
    font-size: 16px;
    margin: 8px 0 0;
  }
  .wordmark--side {
    left: 42px;
    top: 39px;
    font-size: 32px;
    writing-mode: vertical-rl;
  }
  .side-copy {
    position: absolute;
    left: 24px;
    top: 231px;
    height: 345px;
    margin: 0;
    writing-mode: vertical-rl;
    font-family: "Arimo", sans-serif;
    font-size: 14px;
    line-height: 17px;
    color: var(--ink-light);
  }
</style>
</head>
<body>
  <main class="canvas">
    <section class="label" aria-label="Sparkling water bottle label">
      <h1 class="wordmark wordmark--hero">Villa Serena</h1>
      <div class="product-info">
        <p class="product-info__type">SPARKLING<br>WATER</p>
        <p class="product-info__volume">375mL</p>
      </div>
      <p class="wordmark wordmark--side">Villa Serena</p>
      <p class="side-copy">Lorem ipsum dolor sit amet, consectetur adipiscing elit. Morbi ultricies molestie orci. Aenean purus mauris, sodales nec diam dignissim, porttitor</p>
    </section>
  </main>
</body>
</html>
```